My dynamic new collection of short plays needs an eye catching web-based ad!

I am buying ad space on a theater magazine's website with these specs for a new book. The ad will run for a few months. I have the book cover - which will be the main image, but need the ad designed with quotes and the publisher's logo. Here are the specs:
230 pixels wide x 250 pixels high
72 dpi

Target Market(s)

Theater artists and theater educators

Industry/Entity Type

Theater / Education

Font styles to use
Sans Serif
Other font styles liked:
• Please use fonts that match the book cover. I'm including an ad that is currently on the website where I will be advertising. It is not the size that I'm going for, but it contains the elements that I want. I'm also including an image of the logo of the publisher, and I have other versions of this logo (other formats / larger size) that I can deliver if needed.

Requirements
Must have
• Simple compelling image with a quote from the book and a link to the publisher website. A compelling quote (or two) from the book jacket. The name and logo of the publisher.
Nice to have
• Some eye catching color to compliment the beautiful cover design
Should not have
• Too much busy-ness in the image or the presentation.

```html
<!DOCTYPE html>
<html lang="en">
<head>
<meta charset="utf-8">
<title>A Few Short Plays to Mend the World — Book Ad</title>
<link rel="stylesheet" href="https://fonts.googleapis.com/css2?family=Montserrat:wght@500;600;700;800&display=swap">
<style>
  :root {
    --royal-blue: #05229a;
    --cover-deep: #1a3bb0;
    --cover-light: #3fa6e6;
    --ink: #111111;
    --rule: #2a2a2a;
    --paper: #ffffff;
    --logo-gray: #3a3a3a;
  }
  * { box-sizing: border-box; margin: 0; padding: 0; }
  html, body {
    width: 1200px; height: 1200px; overflow: hidden;
    background: var(--paper);
    font-family: "Montserrat", Arial, sans-serif;
  }
  .ad {
    position: relative; width: 1200px; height: 1200px;
    background: var(--paper); overflow: hidden;
  }
  .ad__band { position: absolute; inset: 0; }
  .book {
    position: absolute; left: 50px; top: 125px; width: 480px; height: 770px;
  }
  .book__pages {
    position: absolute; left: 480px; top: 14px; width: 46px; height: 740px;
    background: linear-gradient(90deg, #e6e6e6, #f7f7f7);
    border-right: 8px solid var(--royal-blue);
  }
  .book__cover {
    position: absolute; inset: 0;
    background: radial-gradient(circle at 45% 40%, var(--cover-light) 0%, var(--cover-deep) 55%, #0f2a8c 100%);
    box-shadow: 0 18px 30px rgba(0,0,0,0.22);
  }
  .title {
    position: absolute; left: 627px; top: 360px;
    color: var(--paper); font-weight: 800; font-size: 64px;
    line-height: 76px; letter-spacing: 0.5px; text-transform: uppercase;
  }
  .author {
    position: absolute; left: 638px; top: 680px; right: 0;
    display: flex; align-items: center; gap: 10px;
    color: var(--paper); font-weight: 600; font-size: 24px;
    letter-spacing: 11px; text-transform: uppercase;
  }
  .author__rule { flex: 1; height: 2px; background: var(--paper); }
  .publisher {
    position: absolute; left: 40px; top: 945px; width: 200px;
    display: flex; flex-direction: column; align-items: center; gap: 14px;
  }
  .publisher__mark {
    width: 120px; height: 120px; border-radius: 50%; background: var(--logo-gray);
  }
  .publisher__name {
    color: var(--logo-gray); font-weight: 500; font-size: 15px;
    letter-spacing: 2px; text-transform: uppercase; text-align: center; line-height: 1.4;
  }
  .quote {
    position: absolute; left: 260px; top: 960px; width: 684px; text-align: center;
  }
  .quote__rule {
    display: flex; align-items: center; gap: 12px; height: 24px;
  }
  .quote__rule::before, .quote__rule::after {
    content: ""; flex: 1; height: 1.5px; background: var(--rule);
  }
  .quote__mark {
    color: var(--royal-blue); font-weight: 800; font-size: 44px; line-height: 24px;
    height: 24px; overflow: hidden; padding-top: 6px;
  }
  .quote__text {
    color: var(--ink); font-weight: 600; font-size: 23px; line-height: 34px;
    margin: 2px 0 4px;
  }
  .quote__name {
    margin-top: 12px; color: var(--royal-blue); font-weight: 700; font-size: 18px;
  }
  .quote__role { color: var(--ink); font-weight: 500; font-size: 17px; margin-top: 4px; }
  .cta {
    position: absolute; left: 986px; top: 952px; width: 160px; height: 160px;
    border-radius: 50%; background: var(--royal-blue);
    display: flex; align-items: center; justify-content: center; text-align: center;
    color: var(--paper); font-weight: 800; font-size: 38px; line-height: 42px;
    text-decoration: none;
  }
</style>
</head>
<body>
<main class="ad">
  <svg class="ad__band" width="1200" height="1200" viewBox="0 0 1200 1200" aria-hidden="true">
    <polygon points="0,413 1200,157 1200,916 0,657" fill="var(--royal-blue)"/>
  </svg>

  <div class="book">
    <div class="book__pages"></div>
    <div class="book__cover" role="img" aria-label="Book cover: colourful mosaic portrait of the author on a swirling blue background with the title and author name"></div>
  </div>

  <h1 class="title">A Few<br>Short Plays<br>to Mend the<br>World</h1>

  <p class="author"><span>Marcus Ellery</span><span class="author__rule"></span></p>

  <div class="publisher">
    <span class="publisher__mark"></span>
    <span class="publisher__name">Quiet Heron Press</span>
  </div>

  <figure class="quote">
    <div class="quote__rule"><span class="quote__mark">&ldquo;</span></div>
    <blockquote class="quote__text">Marcus provokes us to look more carefully at systems of race and power and our participation in them in ways that linger long after the blackout.</blockquote>
    <div class="quote__rule"><span class="quote__mark">&rdquo;</span></div>
    <figcaption>
      <p class="quote__name">Dana Whitfield</p>
      <p class="quote__role">Artistic Director, Bright Lantern Theatre</p>
    </figcaption>
  </figure>

  <a class="cta" href="#">Buy<br>Now</a>
</main>
</body>
</html>
```